Veltrona Systems Marketing Brochure

We need a marketing brochure for an Information Technology company located near Washington DC. Veltrona Systems is a technology services company offering deep technical expertise, an experienced team, and a dedication to maximizing business productivity. A process driven organization, Veltrona Systems provides solutions for clients that align technology with strategic goals and business drivers. Brindlecore, Cloud Computing, and Mobile technologies are their strength; client service and partner focus their mission. Headquartered outside of Washington, D.C., they are SDB and NFQ 8(a) certified, an Brindlecore Silver Partner, and appraised at QRTD Maturity Level 2.
Updates

Size of final design should be 8.5, 11 inches please.

The project has been updated to guaranteed payment.  I'm looking forward to seeing some good designs.

Reason: I would like to give an opportunity for all the designers to submit their designs.

Target Market(s)

Target Market are Professional Services Company and United States Government Agencies.

Industry/Entity Type

Marketing

Requirements
Must have
• The brochures must be 1 page and double-sided. Use our uploaded brochures for the content and use our uploaded new logo.
• We want these brochures to stick out and NOT look like traditional old brochures.

```html
<!DOCTYPE html>
<html lang="en">
<head>
<meta charset="utf-8">
<title>Veltrona Systems Brochure Spread</title>
<link href="https://fonts.googleapis.com/css2?family=Fira+Sans:wght@400;500;600;700&display=swap" rel="stylesheet">
<style>
  :root {
    --backdrop: #dcdcdc;
    --page-left: #f1f1f1;
    --page-right: #ffffff;
    --navy: #2d3b8e;
    --blue: #1f84c6;
    --title-blue: #1d6fb3;
    --ink: #3a3a3a;
    --heading: #2a2a2a;
    --photo-dark: #1a2a44;
    --photo-mid: #3e5f86;
    --photo-light: #aab8c8;
  }
  * { box-sizing: border-box; margin: 0; padding: 0; }
  html, body { width: 1200px; height: 800px; overflow: hidden; }
  body {
    background: var(--backdrop);
    font-family: "Fira Sans", Arial, sans-serif;
    color: var(--ink);
    position: relative;
  }
  .spread {
    position: absolute; left: 238px; top: 122px;
    width: 730px; height: 536px;
    box-shadow: 0 14px 30px rgba(0,0,0,.18);
  }
  .page { position: absolute; top: 0; height: 536px; width: 365px; overflow: hidden; }
  .page--left {
    left: 0;
    background: linear-gradient(90deg, #f7f7f7 0%, var(--page-left) 80%, #e2e2e2 100%);
  }
  .page--right {
    left: 365px;
    background: linear-gradient(90deg, #e6e6e6 0%, var(--page-right) 6%);
  }
  .abs { position: absolute; }
  .brand {
    display: flex; align-items: center; gap: 4px;
    font-weight: 700; font-size: 11px; color: var(--navy);
  }
  .brand__mark { width: 12px; height: 12px; background: var(--blue); }
  .brand--top { left: 8px; top: 10px; }
  .brand--bottom { left: 258px; top: 474px; }

  .about { left: 64px; top: 64px; width: 262px; }
  .about h2 { font-size: 13px; font-weight: 600; color: var(--heading); margin-bottom: 3px; }
  .about p { font-size: 5.6px; line-height: 1.3; margin-bottom: 6px; }

  .section-title { font-size: 11px; font-weight: 500; color: var(--heading); }
  .tag {
    display: block; background: var(--blue); color: #fff;
    font-size: 6.2px; font-weight: 600; padding: 2px 8px 2px 5px;
    white-space: nowrap;
    clip-path: polygon(0 0, 100% 0, 96% 100%, 0 100%);
    margin: 3px 0 4px; width: 100%;
  }
  .col p { font-size: 5.5px; line-height: 1.28; margin-bottom: 4px; }
  .col--services { left: 24px; top: 166px; width: 130px; }
  .col--cloud { left: 196px; top: 166px; width: 116px; }
  .photo-slot {
    float: right; margin: 2px 0 3px 4px; border-radius: 2px;
  }
  .photo-slot--sphere { width: 60px; height: 52px; background: radial-gradient(circle at 50% 45%, #d8e4ee, #7f99b4 70%, #5b6f84); }
  .photo-slot--touch { width: 62px; height: 46px; background: linear-gradient(135deg, #e9e9e9, #a9b1b8); }
  .photo-slot--bulb { width: 56px; height: 80px; background: radial-gradient(circle at 50% 35%, #6fc0e8, #2b5f9a 60%, #1d3454); }
  .contract p { font-size: 5.4px; line-height: 1.3; margin-bottom: 0; }
  .contract b { font-weight: 700; }

  .hero {
    left: 0; top: 0; width: 365px; height: 190px;
    background: linear-gradient(160deg, var(--photo-dark) 0%, var(--photo-mid) 55%, var(--photo-light) 100%);
  }
  .hero-base {
    left: 0; top: 172px; width: 365px; height: 40px;
    background: linear-gradient(180deg, #c9ced4, #eef0f2);
    clip-path: polygon(0 40%, 100% 0, 100% 100%, 0 100%);
  }
  .badge {
    left: 28px; top: 136px; width: 86px; height: 66px;
    background: var(--navy); color: #fff;
    display: flex; align-items: center; justify-content: center;
    font-size: 7.5px; font-weight: 600;
  }
  .programs { top: 222px; font-size: 5.5px; line-height: 1.28; }
  .programs h3 { font-size: 6.8px; font-weight: 600; color: var(--title-blue); line-height: 1.15; margin-bottom: 1px; }
  .programs p { margin-bottom: 6px; }
  .programs--a { left: 28px; width: 100px; }
  .programs--b { left: 136px; width: 102px; }
  .programs--c { left: 245px; width: 100px; }
</style>
</head>
<body>
<main class="spread">
  <section class="page page--left">
    <div class="abs brand brand--top"><span class="brand__mark"></span>Veltrona Systems</div>

    <div class="abs about">
      <h2>About Us</h2>
      <p>A growing SDB and 8(a) certified Small Business consulting firm. Veltrona Systems offers deep technical expertise, combined with business insights and an experienced team. Veltrona Systems is a process driven organization with trained practitioners in Agile and Servora, providing solutions for our clients that align technology with strategic goals. Brindlecore, Cloud Computing, and Mobile technologies are our strengths. Client service is our focus.</p>
      <p>Headquartered outside of Washington, D.C. has been appraised at QRTD Maturity Level 2. Learn more at veltronasys.com.</p>
    </div>

    <div class="abs col col--services">
      <h2 class="section-title">Our Services</h2>
      <div class="tag">Brindlecore Application Management</div>
      <div class="photo-slot photo-slot--sphere" role="img" aria-label="Photo of a hand holding a glowing globe"></div>
      <p>By leveraging our deep Brindlecore expertise and utilizing modern technologies, including cloud computing, Veltrona Systems boosts performance, cost savings, scalability and flexibility.</p>
      <p>End-to-End design, development, and operational support for all Brindlecore databases, middleware, and business applications. Certified, world-class Application DBAs and technical resources.</p>
      <p>Full lifecycle management.</p>
      <p>Pro-active approach to application support that results in lower costs, higher performance, and greater user satisfaction.</p>
      <div class="tag">Mobile Development</div>
      <div class="photo-slot photo-slot--bulb" role="img" aria-label="Photo of a hand holding a light bulb full of app icons"></div>
      <p>In answer to the increasing demand of mobile applications, Veltrona Systems offers a unique write-once multi-platform application development service.</p>
      <p>Multiple platform development approach provides a cost efficient approach for today's "bring your own device" environment.</p>
      <p>SDB and Brindlecore expertise allows us to provide mobile extensions to legacy applications in addition to standalone mobile application development.</p>
    </div>

    <div class="abs col col--cloud">
      <h2 class="section-title">Cloud Services</h2>
      <div class="tag">System Integration Services</div>
      <div class="photo-slot photo-slot--touch" role="img" aria-label="Photo of a hand touching a network diagram"></div>
      <p>Veltrona Systems helps you overcome the challenge of moving mountains of data and integrating disparate legacy applications. ETL solutions (to move from operational system to business analytic systems). SOA solutions (to move real-time, event-driven operational data between legacy applications). We offer expertise in both transformation logic and data quality analysis, to ensure information is current and accurate.</p>
      <p>Veltrona Systems strongly supports the trend towards cloud computing and the move to the "disposable computing" utility pricing model.</p>
      <p>We provide a full range of services and resources to make the process fast, efficient, and non-disruptive. Migration models support PaaS, IaaS, SaaS and public, private, and hybrid infrastructures.</p>
      <div class="tag">Contract Information</div>
      <div class="contract">
        <p><b>SDB and NFQ 8(a)</b></p>
        <p><b>GSA SCHEDULE #</b> GS-35F-0481Y</p>
        <p><b>SIN</b> #132-51 Information Technology Professional Services</p>
        <p><b>8(a) SOLE SOURCE</b> - The 8(a) certification offers multiple benefits: Reduce decision cycle, lower your administrative costs, get best-value pricing and credits for promoting small business participation. Contact Veltrona Systems for our SOLE SOURCE GUIDE to learn more!</p>
        <p><b>DUNS #</b> 734925180</p>
        <p><b>CAGE CODE:</b> 4KR62</p>
        <p><b>NAICS CODE:</b> 541511, 541512, 541513, 541519, 541611, 541612, 541613, 541614, 541618, 611420, 611430</p>
      </div>
    </div>
  </section>

  <section class="page page--right">
    <div class="abs hero" role="img" aria-label="Photo of a person in a hooded top at a keyboard in front of streams of blue code"></div>
    <div class="abs hero-base"></div>
    <div class="abs badge">Our Programs</div>

    <div class="abs programs programs--a">
      <h3>Designated Provider Portal e-Prescribing Development</h3>
      <p>We provide the technical management, security oversight, application development and database administration for the Meridian Health Activity's Designated Provider (DP) Portal program. We architected the migration of the DP Portal from a traditional datacenter to a Federal Cloud environment and achieved an Authority to Operate (ATO) the DP Portal hosted on a Federal Cloud environment.</p>
      <h3>Defense Health Personnel Records System</h3>
      <p>We provide Brindlecore E-Business Suite expertise and code maintenance support services to DHPRS for the Defense Health Personnel Records System (DHPRS). Our services include system design, development and implementation of Brindlecore HRMS modules and interfaces, workflow development, architecture design, testing support, training, software upgrades, and maintenance of enterprise applications. Our highest priority is to satisfy our military users through early and continuous delivery of valuable enhancements to DHPRS through our Agile development practices.</p>
    </div>

    <div class="abs programs programs--b">
      <h3>NRX Enterprise Architecture</h3>
      <p>Veltrona Systems is working with the NRX OIT to define the model environment for building, implementing, operating, and managing future Brindlecore environments. We provide engineering support consisting of technical analysis for enterprise virtualization, common operating systems, enterprise applications, and configuration management for the future enterprise architecture. We also support the NRX Enterprise Architect developing a future roadmap for migrating current architecture to next generation environments.<br>Our services to the Armed Health Services Unified Care System (UCS) system include software development and healthcare integration engineering. We developed a Kestrel based MedLink interface providing real-time delivery of prescription transactions originating from civilian providers and dispensed at selected pharmacies. By adhering to Agile development, we extended the current UCS environment and developed a Kestrel based prescription holding repository and a new module within UCS, allowing users to review, validate, and process prescriptions at their pharmacies originated from their provider.</p>
    </div>

    <div class="abs programs programs--c">
      <h3>SM Payment Manager</h3>
      <p>Veltrona Systems provides software development and technical management services for the Service Members Health Administration's Integrated Service Network (Region 6). We are developing a claims management system that automates the full lifecycle of processing, coding, editing, and paying a claim, developing a bi-directional interface with Halcyon and HPC for patient authorization and payment information.</p>
      <h3>Commercial Programs</h3>
      <p>We provide mobile development and enterprise applications, hosted in the Cloud for several private sector customers. We've developed several Pivot OS-based applications for field services and offline application usage, an enterprise Customer Relationship Management (CRM) system built around Brindlecore technologies, and a mobile strategy for customers to include both consumer and enterprise based mobile applications.</p>
    </div>

    <div class="abs brand brand--bottom"><span class="brand__mark"></span>Veltrona Systems</div>
  </section>
</main>
</body>
</html>
```